the theater production needs a poster design

we
we need a poster design for the Opera 'Tobin and Marigold'
the show will be put on the stage on May 18.
the week is family week.
we launch the Opera on the stage size of 700 people
the opera will be performed by Orchestra of 30 musicians and 7 singers
most of audience are parents with children.
we will use the final design for the printing and mobile marketing.

here is the informations

Opera 'Tobin and Marigold'

date: 2024.5.18 Saturday 2pm, 5pm
Seoryeon Arthall
Ticket $50
BOOK _02-735-6089
Music Director_Yuna Seo, Producer Taeho Park

```html
<!DOCTYPE html>
<html lang="en">
<head>
<meta charset="utf-8">
<title>Opera Tobin &amp; Marigold – Poster</title>
<link rel="stylesheet" href="https://fonts.googleapis.com/css2?family=Fira+Sans:wght@400;500;600;700&display=swap">
<style>
  :root {
    --page-bg: #e9e9ea;
    --poster-top: #3f2628;
    --poster-mid: #6e2229;
    --poster-bottom: #8a2530;
    --seat-red: #c21f2e;
    --ink-white: #ffffff;
    --ink-black: #111111;
  }
  * { box-sizing: border-box; margin: 0; padding: 0; }
  html, body {
    width: 1200px; height: 1200px; overflow: hidden;
    background: var(--page-bg);
    font-family: "Fira Sans", Arial, sans-serif;
  }
  .poster {
    position: absolute; left: 220px; top: 62px;
    width: 760px; height: 1075px; overflow: hidden;
    color: var(--ink-white);
  }
  .poster-photo {
    position: absolute; inset: 0;
    background:
      radial-gradient(ellipse 70% 30% at 70% 55%, rgba(194,31,46,0.45), transparent 70%),
      radial-gradient(ellipse 60% 25% at 30% 80%, rgba(194,31,46,0.35), transparent 70%),
      linear-gradient(180deg, var(--poster-top) 0%, #5a2428 30%, var(--poster-mid) 55%, var(--poster-bottom) 100%);
  }
  .title-block {
    position: absolute; left: 60px; top: 150px; width: 680px; height: 300px;
    transform: rotate(-7.5deg); transform-origin: 50% 50%;
  }
  .title-word { position: absolute; left: 0; top: 0; overflow: visible; }
  .title-word text {
    font-family: "Fira Sans", Arial, sans-serif;
    font-weight: 400; font-size: 226px;
    fill: rgba(60, 20, 22, 0.35);
    stroke: var(--ink-white); stroke-width: 3;
  }
  .show-band {
    position: absolute; left: 250px; top: 218px;
    width: 420px; height: 56px;
    background: var(--ink-white); color: var(--ink-black);
    font-weight: 600; font-size: 40px; line-height: 56px;
    text-align: center; white-space: nowrap;
  }
  .show-info { position: absolute; left: 0; width: 100%; text-align: center; }
  .show-date { top: 532px; font-size: 27px; font-weight: 400; line-height: 36px; }
  .venue { top: 646px; font-size: 40px; font-weight: 700; letter-spacing: 1.5px; }
  .ticket {
    position: absolute; left: 195px; top: 762px; width: 370px; height: 100px;
  }
  .ticket-shape { position: absolute; inset: 0; }
  .ticket-label {
    position: absolute; inset: 0;
    color: var(--ink-black);
    font-size: 64px; font-weight: 500; line-height: 100px; text-align: center;
  }
  .booking { top: 896px; font-size: 36px; font-weight: 700; letter-spacing: 0.5px; }
  .credits { top: 986px; font-size: 25px; font-weight: 400; }
  .credits strong { font-weight: 600; }
</style>
</head>
<body>
  <main class="poster">
    <div class="poster-photo" role="img" aria-label="Photo of curved rows of red theatre seats in a dim concert hall"></div>

    <div class="title-block">
      <svg class="title-word" width="680" height="240" viewBox="0 0 680 240" aria-label="Opera">
        <text x="0" y="200">Opera</text>
      </svg>
      <div class="show-band">Tobin &amp; Marigold</div>
    </div>

    <p class="show-info show-date">2024.5.18 Saturday<br>2pm, 5pm</p>
    <p class="show-info venue">SEORYEON ARTHALL</p>

    <div class="ticket">
      <svg class="ticket-shape" width="370" height="100" viewBox="0 0 370 100" aria-hidden="true">
        <defs>
          <pattern id="stamp-holes" x="-5" y="-5" width="10" height="10" patternUnits="userSpaceOnUse">
            <circle cx="5" cy="5" r="4" fill="#000"/>
          </pattern>
          <mask id="stamp-edge" maskUnits="userSpaceOnUse" x="0" y="0" width="370" height="100">
            <rect width="370" height="100" fill="#fff"/>
            <rect x="0" y="0" width="370" height="5" fill="url(#stamp-holes)"/>
            <rect x="0" y="95" width="370" height="5" fill="url(#stamp-holes)"/>
            <rect x="0" y="0" width="5" height="100" fill="url(#stamp-holes)"/>
            <rect x="365" y="0" width="5" height="100" fill="url(#stamp-holes)"/>
          </mask>
        </defs>
        <rect width="370" height="100" fill="#ffffff" mask="url(#stamp-edge)"/>
      </svg>
      <span class="ticket-label">Ticket $50</span>
    </div>

    <p class="show-info booking">BOOK _02-735-6089</p>
    <p class="show-info credits"><strong>Music Director</strong>_Yuna Seo, Producer Taeho Park</p>
  </main>
</body>
</html>
```